Now hiring billboard for roofing company

We would like to design/slogan for a "now hiring" billboard for a variety of positions in our roofing company.
We perform residential and commercial roofing.
We are looking to hire roofers, laborers, gutter installers, sheet metal workers, commercial drivers, commercial roofers, and residential and commercial service technicians.
Looking to attract both entry level and experienced roofers.
Roofing is a good industry to build a career, learn a trade, we provide training.

Opportunity to learn a trade and move from unskilled to skilled positions.
Use Brandell Roofing as a stepping stone in your career.

Brandell Roofing is a stable, growing company that has been providing roofing services in the Portland area for over 35 years. We have a great team of employees, many with over 10 years with the company.
In addition to roofing homes, our Residential Department also offers repair and cleaning services as well as gutter installation and repair.
In 2014 we added a dedicated Commercial Department that services commercial customers with roofing projects and service/repairs. In addition, they offer the Brandell topGuard maintenance program.
Mostly recently Brandell Roofing purchased Corvasse Sheet Metal (CSM) in 2016. CSM specializes in custom metal fabrication, continuous gutters and custom copper fabrication.

If you are looking for a job where you are appreciated
at a company that values honesty and respect,
come and join our team!
Whether you are experienced or just wanting to
learn, we are looking to add hard-working, reliable
go-getters to our team. We offer a flexible work
environment and in addition to full-time work offer
part-time and summer positions.
We are always looking to add great people to our
team. Some of the job/career options are:
• Residential Roofer
• Commercial Roofer
• Gutter Installer
• Service Technician
• Sheet Metal Fabricator/Installer
• Commercial Driver
• General Labor

Brandell Roofing offers competitive pay and an excellent benefits package.

Join our team today!

Target Market(s)

Job seekers

Font styles to use
Serif

Colors

Designer to choose colors to be used in the design.

Requirements
Must have
• Get across that we are hiring and have our contact info
• CCB #61834
• brandellwork.example
Nice to have
• Simple, easy to understand regardless of language literacy.
• Have a high proportion of Hispanic workers, maybe include Spanish.
• Spanish hiring phone number is 503-648-9013

```html
<!DOCTYPE html>
<html lang="en">
<head>
<meta charset="utf-8">
<title>Brandell Roofing – Now Hiring Billboard</title>
<link rel="stylesheet" href="https://fonts.googleapis.com/css2?family=Montserrat:wght@400;500;600;800&family=Oswald:wght@700&display=swap">
<style>
  :root {
    --orange: #ef7f2a;
    --orange-light: #f8b24a;
    --coral: #f0705a;
    --navy: #4f5872;
    --black: #0b0b0b;
    --footer-grey: #d3d3d3;
    --line-grey: #c8c8c8;
    --white: #ffffff;
    --stage: #e6e6e6;
  }
  * { margin: 0; padding: 0; box-sizing: border-box; }
  html, body { width: 1200px; height: 558px; overflow: hidden; }
  body { background: var(--stage); font-family: "Montserrat", Arial, sans-serif; position: relative; }

  .billboard { position: absolute; left: 28px; top: 42px; width: 1144px; height: 458px; background: var(--white); overflow: hidden; }
  .billboard-shapes { position: absolute; inset: 0; width: 1144px; height: 458px; }

  .brand-name { position: absolute; left: 0; top: 92px; width: 842px; text-align: center; font-weight: 800; font-size: 60px; line-height: 1; color: var(--orange); letter-spacing: -1px; white-space: nowrap; }

  .hiring-title { position: absolute; left: 27px; top: 196px; height: 66px; font-family: "Oswald", Impact, sans-serif; font-weight: 700; font-size: 46px; line-height: 66px; color: var(--white); white-space: nowrap; }
  .hiring-tagline { position: absolute; left: 280px; top: 208px; font-weight: 600; font-size: 16.5px; line-height: 21px; color: var(--white); white-space: nowrap; }

  .intro { position: absolute; left: 28px; top: 273px; font-size: 15.2px; line-height: 18px; color: var(--navy); white-space: nowrap; }

  .job-list { position: absolute; left: 0; top: 0; width: 760px; height: 458px; list-style: none; pointer-events: none; }
  .job-list li { position: absolute; font-size: 15px; line-height: 18px; color: var(--navy); padding-left: 16px; white-space: nowrap; }
  .job-list li::before { content: ""; position: absolute; left: 0; top: 5px; width: 8px; height: 8px; border-radius: 50%; background: var(--orange); }

  .licence { position: absolute; left: 481px; top: 376px; font-size: 15px; line-height: 18px; font-weight: 600; color: var(--orange); white-space: nowrap; }

  .contact-bar { position: absolute; left: 0; top: 414px; height: 44px; width: 790px; }
  .contact-item { position: absolute; top: 13px; display: flex; align-items: center; gap: 5px; font-size: 12px; line-height: 16px; color: var(--black); white-space: nowrap; }
  .contact-item svg { width: 15px; height: 15px; flex: none; }

  .website { position: absolute; left: 813px; top: 398px; width: 200px; text-align: center; color: var(--white); }
  .website svg { width: 24px; height: 24px; display: block; margin: 0 auto 8px; }
  .website span { display: block; font-size: 11px; line-height: 14px; letter-spacing: 1px; }
</style>
</head>
<body>
<main class="billboard">
  <svg class="billboard-shapes" viewBox="0 0 1430 572" preserveAspectRatio="none">
    <defs>
      <linearGradient id="photoTones" x1="0" y1="0" x2="0.6" y2="1">
        <stop offset="0" stop-color="#c7def0"/>
        <stop offset="0.3" stop-color="#6f8f4d"/>
        <stop offset="0.55" stop-color="#c98552"/>
        <stop offset="1" stop-color="#e08a4a"/>
      </linearGradient>
    </defs>
    <rect class="side-strip" x="0" y="0" width="20" height="517" fill="var(--orange)"/>
    <rect class="corner-block" x="0" y="517" width="20" height="55" fill="var(--black)"/>
    <polygon class="hiring-band" points="20,245 940,245 970,287 940,327 20,327" fill="var(--orange)"/>
    <rect class="contact-strip" x="20" y="517" width="1020" height="55" fill="var(--footer-grey)"/>
    <polygon class="grey-rule" points="960,0 980,0 1130,152 1118,162" fill="var(--line-grey)"/>
    <polygon role="img" aria-label="Photo of a roofer in a safety harness climbing an orange tiled roof" points="1140,150 1295,0 1430,0 1430,572 1295,572 1140,420 1020,287" fill="url(#photoTones)"/>
    <polygon class="top-wedge" points="985,0 1295,0 1140,150" fill="var(--black)"/>
    <polygon class="bottom-wedge" points="985,572 1295,572 1140,420" fill="var(--black)"/>
    <polygon class="accent-stripe" points="1300,0 1325,0 1160,165 1145,150" fill="var(--orange-light)"/>
    <polygon class="chevron-outer" points="1095,160 1135,160 1000,287 1135,415 1095,415 960,287" fill="var(--orange-light)"/>
    <polygon class="chevron-inner" points="1138,152 1152,152 1032,287 1152,425 1138,425 1018,287" fill="var(--coral)"/>
  </svg>

  <h1 class="brand-name">Brandell Roofing</h1>

  <h2 class="hiring-title">NOW HIRING</h2>
  <p class="hiring-tagline">ROOFING IS A GOOD INDUSTRY TO BUILD A CAREER,<br>LEARN A TRADE, WE PROVIDE TRAINING</p>

  <p class="intro">We are always looking to add great people to our team. Some of the job / career options are :</p>

  <ul class="job-list">
    <li style="left:32px;top:318px">Residential Roofer</li>
    <li style="left:32px;top:347px">Commercial Roofer</li>
    <li style="left:32px;top:376px">Gutter Installer</li>
    <li style="left:261px;top:318px">Service Technician</li>
    <li style="left:261px;top:347px">Commercial Driver</li>
    <li style="left:481px;top:318px">Sheet Metal Fabricator / Installer</li>
    <li style="left:481px;top:347px">General Labor</li>
  </ul>
  <p class="licence">CCB #61834</p>

  <footer class="contact-bar">
    <div class="contact-item" style="left:32px">
      <svg viewBox="0 0 16 16"><circle cx="8" cy="8" r="8" fill="#111"/><path d="M8 3.5a3 3 0 0 0-3 3c0 2.2 3 6 3 6s3-3.8 3-6a3 3 0 0 0-3-3zm0 4.2a1.2 1.2 0 1 1 0-2.4 1.2 1.2 0 0 1 0 2.4z" fill="#fff"/></svg>
      4170 SW Kestrel Lane, Tualatin, OR 97062
    </div>
    <div class="contact-item" style="left:370px">
      <svg viewBox="0 0 16 16"><circle cx="8" cy="8" r="8" fill="#111"/><path d="M5.3 4c.3-.2.6-.1.8.2l.8 1.4c.1.3 0 .6-.2.8l-.5.4c.4.9 1.2 1.7 2.1 2.1l.4-.5c.2-.2.5-.3.8-.2l1.4.8c.3.2.4.5.2.8l-.5.9c-.2.3-.6.5-1 .4C7 10.6 5.4 9 4.9 6.5c-.1-.4.1-.8.4-1z" fill="#fff"/></svg>
      503.555.0142
    </div>
    <div class="contact-item" style="left:502px">
      <svg viewBox="0 0 16 16"><circle cx="8" cy="8" r="8" fill="#111"/><rect x="4.5" y="6" width="7" height="5" rx="0.6" fill="#fff"/><rect x="6" y="4" width="4" height="2.5" fill="#fff"/></svg>
      503.555.0187
    </div>
    <div class="contact-item" style="left:622px">
      <svg viewBox="0 0 16 16"><circle cx="8" cy="8" r="8" fill="#111"/><rect x="4" y="5.2" width="8" height="5.6" rx="0.6" fill="#fff"/><path d="M4.3 5.6 8 8.4l3.7-2.8" stroke="#111" stroke-width="0.9" fill="none"/></svg>
      office@brandell.example
    </div>
  </footer>

  <div class="website">
    <svg viewBox="0 0 24 24" fill="none" stroke="#fff" stroke-width="1.6"><circle cx="12" cy="12" r="10"/><ellipse cx="12" cy="12" rx="4.5" ry="10"/><path d="M2 12h20M4 6.5h16M4 17.5h16"/></svg>
    <span>www.brandellwork.example</span>
  </div>
</main>
</body>
</html>
```